With over 10 years of experience as the president of Brightpath Access Group, LLC, we provide training and consulting services on various accessibility laws and standards, such as the ADA, Section 504, Fair Housing Act, and ANSI A117.1. My company specializes in helping agencies and commercial entities achieve compliance and create an inclusive environment for all customers.

In my role, I conduct ADA self-assessments, consult on transition plans, and deliver training on accessible design, program access, and reasonable accommodations. I use and develop skills such as public speaking, project management, and strategic problem-solving. I value collaboration, innovation, and diversity, and I strive to empower and support my clients and team members in reaching their accessibility goals.

https://brightpathaccessgroup.example/

Target Market(s)

See web site: https://brightpathaccessgroup.example/ or linked in for more language: https://www.linkedin.com/in/tom-hollis-572048163/

Industry/Entity Type

Education and consultative

Other font styles liked:
• Times New Roman

Requirements
Must have
• Specializes in ADA surveys, litigation assistance, construction consultation and transition plans.
Nice to have
• The photos I shared
Should not have
• Any other pictures or negative items

```html
<!DOCTYPE html>
<html lang="en">
<head>
<meta charset="utf-8">
<title>Brightpath Access Group – Flyer</title>
<link href="https://fonts.googleapis.com/css2?family=Cinzel:wght@500;700;900&display=swap" rel="stylesheet">
<style>
  :root{
    --page:#d6d6d6;
    --paper:#eeeff0;
    --sand:#d9d0c3;
    --ink:#48443f;
    --text:#4a4540;
    --white:#ffffff;
  }
  html,body{margin:0;padding:0;width:1200px;height:900px;overflow:hidden;background:var(--page);}
  .flyer{
    position:absolute;left:270px;top:24px;width:660px;height:852px;
    background:var(--paper);overflow:hidden;
    font-family:"Cinzel","Times New Roman",serif;color:var(--text);
    box-shadow:0 6px 18px rgba(0,0,0,.25);
  }
  .brand-tile{position:absolute;left:31px;top:0;width:152px;height:117px;background:var(--sand);
    display:flex;align-items:center;justify-content:center;gap:6px;}
  .brand-dot{width:12px;height:12px;border-radius:50%;background:var(--ink);}
  .brand-name{font-weight:700;font-size:17px;color:var(--ink);letter-spacing:.5px;}
  .headline{position:absolute;right:85px;top:16px;margin:0;text-align:right;
    font-weight:900;font-size:44px;line-height:42px;color:var(--ink);}
  .headline .line-2{font-size:50px;}
  .intro-panel{position:absolute;left:0;top:117px;width:420px;height:261px;background:var(--sand);}
  .intro-text{position:absolute;left:12px;top:198px;width:215px;margin:0;
    font-weight:500;font-size:17.5px;line-height:22px;color:var(--text);}
  .hero-photo{position:absolute;left:229px;top:117px;width:431px;height:261px;
    border-radius:131px 0 0 131px;
    background:linear-gradient(135deg,#6f7f8c 0%,#9fb3c4 40%,#c8d4de 70%,#8e9aa4 100%);}
  .section-title{position:absolute;left:0;top:378px;width:321px;height:100px;background:var(--ink);
    margin:0;box-sizing:border-box;padding:12px 0 0 24px;
    color:var(--white);font-weight:900;font-size:40px;line-height:40px;}
  .services{position:absolute;left:38px;top:522px;margin:0;padding:0;list-style:none;}
  .services::before{content:"";position:absolute;left:9px;top:12px;width:2px;height:134px;background:#c9bfae;}
  .services li{position:relative;height:45px;padding-left:58px;font-weight:500;font-size:21px;line-height:22px;color:var(--ink);}
  .services li::before{content:"";position:absolute;left:0;top:1px;width:20px;height:20px;background:var(--ink);}
  .services li.small{font-size:18px;}
  .gallery{position:absolute;left:0;top:0;}
  .footer-band{position:absolute;left:0;top:0;}
  .contact{position:absolute;left:50px;display:flex;align-items:center;gap:14px;color:var(--white);font-weight:500;}
  .contact.phone{top:766px;font-size:21px;}
  .contact.email{top:805px;font-size:15px;}
  .contact svg{width:22px;height:22px;}
</style>
</head>
<body>
<div class="flyer">
  <div class="brand-tile"><span class="brand-dot"></span><span class="brand-name">Brightpath</span></div>
  <h1 class="headline">DON’T PANIC!<br><span class="line-2">CALL NOW!</span></h1>

  <div class="intro-panel"></div>
  <p class="intro-text">BRIGHTPATH ACCESS GROUP WILL BE WITH YOU FROM THE START UNTIL THE FINISH OF YOUR PROJECT.</p>
  <div class="hero-photo" role="img" aria-label="Photo of a wheelchair user facing a curb on a city street, with an accessibility badge and disability icons"></div>

  <h2 class="section-title">SPECIALIZES<br>IN:</h2>
  <ul class="services">
    <li>ADA SURVEYS</li>
    <li>LITIGATION ASSISTANCE</li>
    <li class="small">CONSTRUCTION CONSULTATION</li>
    <li>TRANSITION PLANS</li>
  </ul>

  <svg class="footer-band" width="660" height="852" viewBox="0 0 660 852">
    <polygon points="0,749 413,749 513,852 0,852" fill="var(--ink)"/>
  </svg>

  <svg class="gallery" width="660" height="852" viewBox="0 0 660 852">
    <defs>
      <linearGradient id="g-site" x1="0" y1="0" x2="1" y2="1"><stop offset="0" stop-color="#8a98a6"/><stop offset=".5" stop-color="#d98a4a"/><stop offset="1" stop-color="#e9e4dc"/></linearGradient>
      <linearGradient id="g-parking" x1="0" y1="0" x2="0" y2="1"><stop offset="0" stop-color="#6e7168"/><stop offset=".55" stop-color="#54575a"/><stop offset="1" stop-color="#6f9fca"/></linearGradient>
      <linearGradient id="g-office" x1="0" y1="0" x2="1" y2="1"><stop offset="0" stop-color="#d8d4cc"/><stop offset=".5" stop-color="#8b6e58"/><stop offset="1" stop-color="#4c4a4c"/></linearGradient>
      <linearGradient id="g-plans" x1="0" y1="0" x2="1" y2="1"><stop offset="0" stop-color="#9fc07a"/><stop offset=".5" stop-color="#f1efe9"/><stop offset="1" stop-color="#dcdcdc"/></linearGradient>
    </defs>
    <g role="img" aria-label="Photo of construction team reviewing plans at a table">
      <polygon points="466,399 540,473 466,547 392,473" fill="url(#g-site)" stroke="var(--ink)" stroke-width="9"/>
    </g>
    <g role="img" aria-label="Photo of accessible parking space with crosswalk markings">
      <polygon points="557,491 631,565 557,639 483,565" fill="url(#g-parking)" stroke="var(--ink)" stroke-width="9"/>
    </g>
    <g role="img" aria-label="Photo of an office meeting including a wheelchair user">
      <polygon points="466,582 540,656 466,730 392,656" fill="url(#g-office)" stroke="var(--ink)" stroke-width="9"/>
    </g>
    <g role="img" aria-label="Photo of a hand drawing on plan sheets">
      <polygon points="557,675 631,749 557,823 483,749" fill="url(#g-plans)" stroke="var(--ink)" stroke-width="9"/>
    </g>
  </svg>

  <div class="contact phone">
    <svg viewBox="0 0 24 24"><path fill="#fff" d="M6.6 10.8a15.1 15.1 0 0 0 6.6 6.6l2.2-2.2c.3-.3.7-.4 1-.2 1.1.4 2.3.6 3.6.6.6 0 1 .4 1 1V20c0 .6-.4 1-1 1A17 17 0 0 1 3 4c0-.6.4-1 1-1h3.5c.6 0 1 .4 1 1 0 1.3.2 2.5.6 3.6.1.3 0 .7-.2 1z"/></svg>
    <span>(555) 014-2287</span>
  </div>
  <div class="contact email">
    <svg viewBox="0 0 24 24" fill="none" stroke="#fff" stroke-width="1.6"><circle cx="12" cy="12" r="9.5"/><ellipse cx="12" cy="12" rx="4.2" ry="9.5"/><line x1="2.5" y1="12" x2="21.5" y2="12"/><path d="M4.5 7h15M4.5 17h15"/></svg>
    <span>INFO@BRIGHTPATHACCESSGROUP.EXAMPLE</span>
  </div>
</div>
</body>
</html>
```